Essential oil label for bottles

Looking to modify our current logo and label design. It looks too simple. I will attach images of our competitors to use as examples. Our company name is Lunvessa. We have 2 different bottles. Clear and amber color. Going forward, we will be using only the amber bottle. The other 2 images are the biggest sellers brands. We want to make some adjustments to ours.

Target Market(s)

Tradeport sales

Industry/Entity Type

Essential oil, perfume

Colors

Designer to choose only greyscale colors for use in the design.

Requirements
Nice to have
• A slight change to fonts and logo design. Maybe change the font and design of the word "Lunvessa" in our logo. Maybe add something to the label to make it stand out more but still keeping it clean and modern
Should not have
• No colors, besides, black, grays, whites, and off white.

```html
<!DOCTYPE html>
<html lang="en">
<head>
<meta charset="utf-8">
<title>Lunvessa Fragrance Oil Label</title>
<link href="https://fonts.googleapis.com/css2?family=Allura&family=Roboto:wght@400;500&display=swap" rel="stylesheet">
<style>
  :root {
    --backdrop: #e2e2e2;
    --label-paper: #f2f1e1;
    --ink: #0b0b0b;
    --ink-reverse: #ffffff;
  }
  html, body {
    margin: 0;
    padding: 0;
    width: 1080px;
    height: 1200px;
    overflow: hidden;
    background: var(--backdrop);
  }
  .canvas {
    position: relative;
    width: 1080px;
    height: 1200px;
  }
  .label {
    position: absolute;
    left: 227px;
    top: 69px;
    width: 626px;
    height: 1062px;
    background: var(--label-paper);
    color: var(--ink);
    font-family: "Roboto", sans-serif;
    overflow: hidden;
  }
  .brand {
    position: absolute;
    left: 83px;
    top: 140px;
    display: flex;
    align-items: center;
    gap: 24px;
  }
  .brand-dot {
    width: 48px;
    height: 48px;
    border: 3px solid var(--ink);
    border-radius: 50%;
    box-sizing: border-box;
  }
  .brand-name {
    font-size: 44px;
    font-weight: 400;
    letter-spacing: 13px;
    text-transform: uppercase;
  }
  .product-name {
    position: absolute;
    left: 0;
    right: 0;
    top: 440px;
    text-align: center;
    font-family: "Allura", cursive;
    font-size: 118px;
    line-height: 1;
    margin: 0;
    font-weight: 400;
    white-space: nowrap;
  }
  .product-type {
    position: absolute;
    left: 50px;
    top: 728px;
    font-size: 46px;
    font-weight: 500;
    letter-spacing: 1.5px;
  }
  .notes-band {
    position: absolute;
    left: 41px;
    right: 0;
    top: 800px;
    height: 72px;
    background: var(--ink);
    color: var(--ink-reverse);
    display: flex;
    align-items: center;
    padding-left: 23px;
    font-size: 33px;
    letter-spacing: 1px;
  }
  .volume {
    position: absolute;
    left: 93px;
    top: 940px;
    font-size: 45px;
    font-weight: 500;
    letter-spacing: 3px;
  }
</style>
</head>
<body>
<main class="canvas">
  <section class="label">
    <div class="brand">
      <span class="brand-dot"></span>
      <span class="brand-name">Lunvessa</span>
    </div>
    <h1 class="product-name">Open Road</h1>
    <div class="product-type">Fragrance Oil</div>
    <div class="notes-band">Oud Wood I leather I Sandalwood</div>
    <div class="volume">200 ML</div>
  </section>
</main>
</body>
</html>
```